Brindle Works Australia Website

Brindle Works Australia (BWA) is a Industrial, Mining & Transport Services provider in Australia. We require a website that is both pc and mobile freindly. The website will be used to both present our company services and give us exposure in a crowded market. The main page of the website will have a snapshot of who BWA is and its from this page that the user can click to enter the area of interest ie. Industrial, Mining and Transport. A disticted logo can be used to indicate the area in question.<br/>Within the industrial, Mining and the Transport services pages will need list and description of services that are provided, current customer lists and news pages.<br/>The website will need a contacts page so prospective customers can get in contact with BWA.<br/>The website design will require a user freindly back end so future updates and ammendments can be carriedout by less experienced people within the BWA business.

Target Market(s)

Industrial, Mining and Transport Services provider markets

Coding

Number of Pages Required

5+ page

Font styles to use
Sans Serif

Colors
00a990

Requirements
Must have
• Ability to build servises with in services. because the main service area is only the main service with in each service group there is alot of smaller services / tasks.
• Key wording for easy seach engine capabilities. The website will need to be search engine freindly.

```html
<!DOCTYPE html>
<html lang="en">
<head>
<meta charset="utf-8">
<title>Brindle Works Australia</title>
<link href="https://fonts.googleapis.com/css2?family=Montserrat:wght@400;500;600;700;900&display=swap" rel="stylesheet">
<style>
:root{
  --green:#00a990;
  --green-dark:#008a75;
  --ink:#111;
  --text:#555;
  --muted:#777;
  --card:#f5f5f5;
  --band:#f3f3f3;
  --line:#e2e2e2;
  --white:#fff;
}
*{margin:0;padding:0;box-sizing:border-box}
html,body{width:1200px;height:3527px;overflow:hidden}
body{position:relative;background:var(--white);font-family:'Montserrat',sans-serif;color:var(--text)}
.abs{position:absolute}
.btn{position:absolute;display:flex;align-items:center;justify-content:center;background:var(--green);color:var(--white);font-size:11px;font-weight:600;letter-spacing:.3px;text-transform:uppercase}
.heading{position:absolute;left:0;width:1200px;text-align:center;font-weight:900;color:var(--ink);font-size:31px}
.rule{position:absolute;display:flex;gap:8px;height:3px}
.rule span{background:var(--green);height:3px}
.rule span:nth-child(1),.rule span:nth-child(3){width:48px}
.rule span:nth-child(2){width:12px}

/* header */
.site-header{position:absolute;left:0;top:0;width:1200px;height:96px;background:var(--white)}
.brand{position:absolute;left:108px;top:22px;display:flex;align-items:center;gap:12px}
.brand-mark{width:40px;height:40px;background:var(--green)}
.brand-name{font-size:22px;font-weight:700;color:var(--green);line-height:1.1}
.nav{position:absolute;right:108px;top:40px;display:flex;gap:33px;font-size:13px;font-weight:500;color:#222}
.nav .active{color:var(--green);font-weight:600}

/* hero */
.hero{position:absolute;left:0;top:96px;width:1200px;height:724px;background:linear-gradient(180deg,#c98a8f 0%,#e0a38a 35%,#6a5c60 65%,#3b3a44 100%);clip-path:path('M0 0 H1200 V642 Q600 820 0 642 Z')}
.hero-panel{position:absolute;left:72px;top:262px;width:606px;height:316px;background:rgba(70,70,70,.55)}
.hero-title{position:absolute;left:108px;top:296px;color:var(--white);font-size:40px;font-weight:900;line-height:1.25}
.hero-text{position:absolute;left:108px;top:413px;width:460px;color:var(--white);font-size:14.5px;line-height:1.8}

/* about */
.about-deco{position:absolute;left:876px;top:1040px;font-size:200px;font-weight:900;color:#edf1f0;line-height:1;letter-spacing:-8px}
.about-text{position:absolute;left:255px;top:978px;width:690px;text-align:center;font-size:13.5px;line-height:1.75}
.divider{position:absolute;left:0;top:1262px;width:1200px;height:1px;background:var(--line)}

/* services */
.card{position:absolute;top:1435px;width:317px;height:543px;background:var(--card)}
.card-art{position:absolute;left:48px;top:36px;width:221px;height:186px;border-radius:4px}
.card-title{position:absolute;left:0;top:243px;width:100%;text-align:center;font-size:20px;font-weight:600;color:var(--ink);line-height:1.3}
.card-text{position:absolute;left:30px;top:306px;width:257px;text-align:center;font-size:12px;line-height:1.75}
.card .btn{left:84px;top:453px;width:150px;height:38px}

/* testimonials */
.testimonials{position:absolute;left:0;top:2069px;width:1200px;height:541px;background:var(--band);overflow:hidden}
.t-deco{position:absolute;left:-10px;top:350px;font-size:200px;font-weight:900;color:#e6e9e8;line-height:1;letter-spacing:-8px}
.quote{position:absolute;left:240px;top:170px;width:720px;text-align:center;font-size:15.5px;line-height:1.95;color:#666}
.avatar{position:absolute;left:558px;top:293px;width:84px;height:84px;border-radius:50%;background:radial-gradient(circle at 50% 40%,#c79a7f,#6d5a52 70%)}
.person{position:absolute;left:0;width:1200px;text-align:center;color:#333}
.dots{position:absolute;left:578px;top:470px;display:flex;gap:8px}
.dots span{width:8px;height:8px;border-radius:50%;background:#ccc}
.dots span.on{background:var(--green)}

/* contact */
.sub-heading{position:absolute;font-size:28px;font-weight:900;color:var(--ink)}
.field{position:absolute;border:1px solid var(--line);background:#fafafa;font-size:11px;color:#888;padding:20px 17px}
.vline{position:absolute;left:682px;top:2780px;width:1px;height:415px;background:#ddd}
.info{position:absolute;left:774px;display:flex;align-items:flex-start;gap:16px;font-size:13px;line-height:1.75;color:#444}
.info svg{flex:none}

/* footer */
.site-footer{position:absolute;left:0;top:3240px;width:1200px;height:287px;background:linear-gradient(180deg,rgba(0,169,144,.15) 0%,var(--green) 45%,var(--green) 100%)}
.footer-brand{position:absolute;left:0;top:3430px;width:1200px;display:flex;justify-content:center;align-items:center;gap:10px}
.footer-brand .brand-mark{width:30px;height:30px;background:var(--white)}
.footer-brand .brand-name{color:var(--white);font-size:18px}
.copyright{position:absolute;left:0;top:3497px;width:1200px;text-align:center;color:var(--white);font-size:12px;font-weight:500}
</style>
</head>
<body>

<header class="site-header">
  <div class="brand"><span class="brand-mark"></span><span class="brand-name">Brindle Works Australia</span></div>
  <nav class="nav">
    <span class="active">HOME</span><span>ABOUT</span><span>SERVICE</span><span>NEWS</span><span>LOCATIONS</span><span>CONTACT</span>
  </nav>
</header>

<section>
  <div class="hero" role="img" aria-label="Photo of a cargo plane, container ship, cranes and a highway at sunset"></div>
  <div class="hero-panel"></div>
  <h1 class="hero-title">Welcome to<br>Brindle Works Australia</h1>
  <p class="hero-text">Lorem ipsum dolor sit amet, consectetur adipisicing elit, sed do eiusmod tempor incididunt ut labore...</p>
  <a class="btn" style="left:108px;top:489px;width:151px;height:38px">Learn More</a>
</section>

<section>
  <div class="about-deco">BWA</div>
  <h2 class="heading" style="top:900px">About BWA</h2>
  <div class="rule" style="left:540px;top:956px"><span></span><span></span><span></span></div>
  <p class="about-text">Lorem ipsum dolor sit amet, consectetur adipisicing elit, sed do eiusmod tempor incididunt ut labore et dolore magna aliqua. Ut enim ad minim veniam, quis nostrud exercitation ullamco laboris nisi ut aliquip ex ea commodo consequat. Duis aute irure dolor in reprehenderit in voluptate velit esse cillum dolore eu fugiat nulla pariatur...</p>
  <a class="btn" style="left:525px;top:1091px;width:150px;height:39px">Learn More</a>
  <div class="divider"></div>
</section>

<section>
  <h2 class="heading" style="top:1326px">Our Services</h2>
  <div class="rule" style="left:540px;top:1389px"><span></span><span></span><span></span></div>

  <article class="card" style="left:108px">
    <div class="card-art" role="img" aria-label="Illustration of an industrial plant with chimneys" style="background:linear-gradient(180deg,#e9f3f1,#1a9c84)"></div>
    <h3 class="card-title">BWA Industrial<br>Services Division</h3>
    <p class="card-text">Offers an integrated site service and maintenance of your fixed plant. Our team are experienced in developing site-specific maintenance / service plans to ensure you critical site equipment stays operational...</p>
    <a class="btn">Learn More</a>
  </article>

  <article class="card" style="left:441px">
    <div class="card-art" role="img" aria-label="Illustration of a mining bulldozer" style="background:linear-gradient(180deg,#e9f3f1,#17907b 60%,#555 100%)"></div>
    <h3 class="card-title">BWA Mining<br>Services Division</h3>
    <p class="card-text">Offers an integrated service in equipment rental, maintenance and earthmoving. Supported by a modern and comprehensive fleet and experienced mechanical technicians that have previous OEM experience...</p>
    <a class="btn">Learn More</a>
  </article>

  <article class="card" style="left:775px">
    <div class="card-art" role="img" aria-label="Illustration of a box truck" style="background:linear-gradient(135deg,#1a9c84,#c9c9d6)"></div>
    <h3 class="card-title">BWA<br>Transport Division</h3>
    <p class="card-text">Specialises in the transportation of all types of materials such as, Steel, Structural Steel, Concrete Building Panels, Machinery, Palletised freight and bulk products.r, all of which are handled with the same amount of care and attention...</p>
    <a class="btn">Learn More</a>
  </article>
</section>

<section class="testimonials">
  <div class="t-deco">BWA</div>
  <h2 class="heading" style="top:90px">Testimonials</h2>
  <div class="rule" style="left:540px;top:151px"><span></span><span></span><span></span></div>
  <p class="quote">“Lorem ipsum dolor sit amet, consectetur adipisicing elit, sed do eiusmod tempor incididunt ut labore et dolore magna aliqua. Ut enim ad minim veniam, quis nostrud exercitation ullamco laboris nisi ut aliquip ex ea commodo consequat.”</p>
  <div class="avatar" role="img" aria-label="Portrait photo of the client"></div>
  <p class="person" style="top:399px;font-size:13px;font-weight:500">Sam Carter</p>
  <p class="person" style="top:423px;font-size:11px">CEO of the Company</p>
  <div class="dots"><span></span><span class="on"></span><span></span></div>
</section>

<section>
  <h2 class="sub-heading" style="left:108px;top:2772px">Get A Quote</h2>
  <div class="rule" style="left:108px;top:2828px"><span></span><span></span><span></span></div>
  <div class="field" style="left:108px;top:2857px;width:233px;height:55px">Name*</div>
  <div class="field" style="left:358px;top:2857px;width:234px;height:55px">Phone*</div>
  <div class="field" style="left:108px;top:2928px;width:233px;height:55px">Email*</div>
  <div class="field" style="left:358px;top:2928px;width:234px;height:55px">Subject*</div>
  <div class="field" style="left:108px;top:3000px;width:484px;height:128px">Message</div>
  <a class="btn" style="left:108px;top:3145px;width:484px;height:50px">Submit</a>

  <div class="vline"></div>

  <h2 class="sub-heading" style="left:774px;top:2772px">Get In Touch</h2>
  <div class="rule" style="left:774px;top:2828px"><span></span><span></span><span></span></div>

  <div class="info" style="top:2858px">
    <svg width="32" height="32" viewBox="0 0 32 32"><circle cx="16" cy="16" r="16" fill="#00a990"/><path d="M16 8a5.5 5.5 0 0 0-5.5 5.5C10.5 18 16 24 16 24s5.5-6 5.5-10.5A5.5 5.5 0 0 0 16 8zm0 7.5a2 2 0 1 1 0-4 2 2 0 0 1 0 4z" fill="#fff"/></svg>
    <span>Unit 4, 18 Quarry Road,<br>Perth WA 6000</span>
  </div>
  <div class="info" style="top:2927px">
    <svg width="32" height="32" viewBox="0 0 32 32"><circle cx="16" cy="16" r="16" fill="#00a990"/><path d="M11.5 9.5l2.5-.5 1.5 3.5-1.7 1.2a9 9 0 0 0 4.5 4.5l1.2-1.7 3.5 1.5-.5 2.5c-.3 1-1.3 1.5-2.3 1.3A12 12 0 0 1 10.2 11.8c-.2-1 .3-2 1.3-2.3z" fill="#fff"/></svg>
    <span style="padding-top:6px">+61 8 5550 1234</span>
  </div>
  <div class="info" style="top:2987px">
    <svg width="32" height="32" viewBox="0 0 32 32"><circle cx="16" cy="16" r="16" fill="#00a990"/><rect x="9" y="11" width="14" height="10" rx="1" fill="#fff"/><path d="M9.5 11.5L16 17l6.5-5.5" stroke="#00a990" stroke-width="1.4" fill="none"/></svg>
    <span style="padding-top:6px">hello@brindleworks.example</span>
  </div>
</section>

<footer>
  <div class="site-footer" role="img" aria-label="Illustrated green city skyline with harbour bridge"></div>
  <div class="footer-brand"><span class="brand-mark"></span><span class="brand-name">Brindle Works Australia</span></div>
  <p class="copyright">© 2020 Brindle Works Australia. All Rights Reserved.</p>
</footer>

</body>
</html>
```